A New and modern Business Card for Talvern Contract Partners Ltd

New and modern Logo and Business Card Attached is the current logo/business card designCurrently the business is called "Talvern & Co." or TCP Ltd for short. This is subject to change.This business specialises in Telecoms and Energy. We work with the major networks (KX, V7, etc) and also offer Energy Products saving clients money off their energy bills.These are business to business services.The current design incorporates a Pheonix, indicating rebirth, starting something new.We would like to maintain the Phoenix element but a newer modern style.We love colours in the logo 3 max.The aim of this is to be ultra slick and modern. I envisage Talvern & Co. on one side of the card with long descriptions on the other side.Side 1:TCP Ltd/Logo?Side 2:TCP Ltd/Logo/Graphic?Brogan & Co.Name:Address:Phone:Email:The design is mostly flexible but must incorporate a Phoenix.For example "Talvern & Co." with a block phoenix behind the text...up to you.

Industry/Entity Type

Telecommunications

Contact Information for Business Card

Talvern & Co.
Address:
Name:
Phone:
Email:

Logo Text

Talvern & Co.

Colors
33a6d7
0792cd
acd037
9bcb3c
f78f20
fece3e

Requirements
Must have
• Phoenix
• 3/4 colours max
• Blue representing Technology (wireless)
• Green for Eco Energy
• Orange for Phoenix
• White business card background
Should not have
• phoenix must not all be red/ orange fire, we are a technology service company and the phoenix colours must represent this. Fire is not representative of our company.

```html
<!DOCTYPE html>
<html lang="en">
<head>
<meta charset="utf-8">
<title>Talvern Contract Partners Ltd – Business Card</title>
<link rel="stylesheet" href="https://fonts.googleapis.com/css2?family=Cinzel:wght@500;600&family=Lato:wght@400;700&display=swap">
<style>
  :root {
    --backdrop: #3b3b3d;
    --card-white: #ffffff;
    --tech-blue: #0792cd;
    --tech-blue-light: #33a6d7;
    --eco-green: #9bcb3c;
    --eco-green-light: #acd037;
    --phoenix-orange: #f78f20;
    --ink: #333333;
    --rule: #d6d6d6;
    --ghost: #ececec;
  }
  * { box-sizing: border-box; margin: 0; padding: 0; }
  html, body { width: 1200px; height: 896px; overflow: hidden; }
  body {
    background: var(--backdrop);
    font-family: "Lato", Arial, sans-serif;
    display: flex;
    align-items: center;
    justify-content: center;
    gap: 40px;
  }
  .card {
    position: relative;
    width: 540px;
    height: 310px;
    overflow: hidden;
    box-shadow: 0 10px 24px rgba(0,0,0,.35);
  }

  /* Front */
  .card-front {
    background: linear-gradient(120deg, var(--tech-blue) 0%, var(--tech-blue-light) 60%, #5fb89a 85%, var(--eco-green) 100%);
  }
  .front-emblem-area {
    position: absolute;
    left: 120px; top: 20px;
    width: 300px; height: 270px;
    border-radius: 50%;
    background: radial-gradient(circle, rgba(255,255,255,.22) 0%, rgba(255,255,255,.1) 50%, rgba(255,255,255,0) 72%);
  }
  .front-wordmark {
    position: absolute;
    left: 0; right: 0; top: 112px;
    text-align: center;
    color: var(--card-white);
    font-family: "Cinzel", Georgia, serif;
    font-weight: 500;
  }
  .front-wordmark .name { font-size: 56px; letter-spacing: 3px; line-height: 1; }
  .front-wordmark .sub { font-size: 15px; letter-spacing: 2.5px; margin-top: 8px; }

  /* Back */
  .card-back { background: var(--card-white); }
  .back-emblem-area {
    position: absolute;
    left: 60px; top: -10px;
    width: 300px; height: 160px;
    border-radius: 50%;
    background: radial-gradient(ellipse, var(--ghost) 0%, rgba(236,236,236,.5) 45%, rgba(255,255,255,0) 72%);
  }
  .contact {
    position: absolute;
    left: 30px; top: 138px;
  }
  .contact .person {
    color: var(--tech-blue);
    font-size: 17px;
    font-weight: 400;
    letter-spacing: 1px;
    text-transform: uppercase;
  }
  .contact .role { color: var(--ink); font-size: 13px; margin-top: 2px; }
  .contact .line {
    display: flex; align-items: center; gap: 8px;
    color: var(--ink); font-size: 13px; margin-top: 8px;
  }
  .contact .line:first-of-type { margin-top: 14px; }
  .contact svg { width: 13px; height: 13px; fill: var(--tech-blue); }

  .logo {
    position: absolute;
    right: 30px; top: 58px;
    width: 240px;
    text-align: center;
    font-family: "Cinzel", Georgia, serif;
    font-weight: 500;
  }
  .logo .mark {
    width: 60px; height: 60px;
    border-radius: 50%;
    background: var(--phoenix-orange);
    margin: 0 auto 10px;
  }
  .logo .name { color: var(--tech-blue); font-size: 40px; letter-spacing: 2px; line-height: 1; }
  .logo .sub { color: var(--eco-green); font-size: 10.5px; font-weight: 600; letter-spacing: 1.5px; margin-top: 5px; }

  .divider {
    position: absolute;
    right: 30px; top: 222px;
    width: 260px; height: 1px;
    background: var(--rule);
  }
  .address {
    position: absolute;
    right: 30px; top: 232px;
    text-align: right;
    color: var(--ink);
    font-size: 13px;
    line-height: 1.5;
  }
  .edge-band {
    position: absolute;
    left: 0; right: 0; bottom: 0;
    height: 9px;
    background: linear-gradient(90deg, var(--tech-blue) 0%, var(--tech-blue-light) 45%, var(--eco-green) 100%);
  }
</style>
</head>
<body>

  <section class="card card-front">
    <div class="front-emblem-area" role="img" aria-label="Soft phoenix emblem watermark"></div>
    <div class="front-wordmark">
      <div class="name">TALVERN</div>
      <div class="sub">CONTRACT PARTNERS LTD</div>
    </div>
  </section>

  <section class="card card-back">
    <div class="back-emblem-area" role="img" aria-label="Faint phoenix emblem watermark"></div>

    <div class="contact">
      <div class="person">Marcus Hale</div>
      <div class="role">Managing Director</div>
      <div class="line">
        <svg viewBox="0 0 24 24" aria-hidden="true"><path d="M6.6 10.8a15.1 15.1 0 0 0 6.6 6.6l2.2-2.2c.3-.3.7-.4 1-.2 1.1.4 2.3.6 3.6.6.6 0 1 .4 1 1V20c0 .6-.4 1-1 1A17 17 0 0 1 3 4c0-.6.4-1 1-1h3.5c.6 0 1 .4 1 1 0 1.3.2 2.5.6 3.6.1.3 0 .7-.2 1z"/></svg>
        <span>044-870 312 645</span>
      </div>
      <div class="line">
        <svg viewBox="0 0 24 24" aria-hidden="true"><path d="M2 5h20v14H2z M3 6l9 7 9-7" stroke="#fff" stroke-width="1.5"/></svg>
        <span>info@talvernco.net</span>
      </div>
    </div>

    <div class="logo">
      <div class="mark"></div>
      <div class="name">TALVERN</div>
      <div class="sub">CONTRACT PARTNERS LTD</div>
    </div>

    <div class="divider"></div>
    <div class="address">
      18 Fenwick Row<br>
      Harlow Vale, 30817
    </div>

    <div class="edge-band"></div>
  </section>

</body>
</html>
```